Business Card and Word .doc header and footer required

I need a business card designed for my cybersecurity consulting company. Also required, is a header and footer to be ued for my word documents.
Attached is the Logo design, font and rgb used.

Industry/Entity Type

Cyber Security Consulting

Contact Information for Business Card

Name, Phone, email, website

Colors
0054AA
0677BA
7BADD7
CADEEF
E8F1F8

Requirements
Must have
• Sleek, modern

```html
<!DOCTYPE html>
<html lang="en">
<head>
<meta charset="UTF-8">
<title>Northgate Cyber — Letterhead</title>
<link href="https://fonts.googleapis.com/css2?family=Poppins:wght@400;700&display=swap" rel="stylesheet">
<style>
  :root {
    --brand-blue: #1a7aab;
    --navy: #172040;
    --faint-blue: #e6f1f5;
    --white: #ffffff;
    --network-line: #3b4d6b;
  }
  * { margin: 0; padding: 0; box-sizing: border-box; }
  html, body { width: 854px; height: 1200px; overflow: hidden; background: var(--white); }
  body { font-family: "Poppins", sans-serif; }
  .letterhead { position: relative; width: 854px; height: 1200px; background: var(--white); overflow: hidden; }

  .brand {
    position: absolute; left: 38px; top: 62px;
    display: flex; align-items: center; gap: 12px;
    color: var(--brand-blue); font-weight: 700; font-size: 26px; letter-spacing: 0.5px;
  }
  .brand-dot { width: 44px; height: 44px; border-radius: 50%; background: var(--brand-blue); }

  .brand-watermark {
    position: absolute; left: 0; right: 0; top: 540px;
    text-align: center; color: var(--faint-blue);
    font-weight: 700; font-size: 92px; line-height: 1.05;
  }

  .footer-band {
    position: absolute; left: 0; top: 1085px; width: 854px; height: 117px;
    background: var(--navy);
  }
  .network-art {
    position: absolute; right: 0; top: 0; width: 350px; height: 100%;
    background: linear-gradient(120deg, rgba(59,77,107,0) 0%, rgba(59,77,107,0.35) 60%, rgba(59,77,107,0.55) 100%);
  }
  .contact {
    position: absolute; display: flex; align-items: center; gap: 10px; color: var(--white);
  }
  .contact-icon {
    width: 31px; height: 31px; border-radius: 50%; background: var(--white);
    display: flex; align-items: center; justify-content: center; flex-shrink: 0;
  }
  .contact-icon svg { width: 18px; height: 18px; }
  .contact-label { font-weight: 700; font-size: 11.5px; line-height: 1.2; }
  .contact-value { font-weight: 400; font-size: 11.5px; letter-spacing: 1.6px; line-height: 1.25; }

  .contact--address { left: 33px; top: 18px; }
  .contact--website { left: 223px; top: 18px; }
  .contact--phone   { left: 33px; top: 63px; }
  .contact--email   { left: 223px; top: 63px; }
</style>
</head>
<body>
<main class="letterhead">
  <header class="brand">
    <span class="brand-dot"></span>
    <span class="brand-name">Northgate Cyber</span>
  </header>

  <div class="brand-watermark" aria-hidden="true">Northgate<br>Cyber</div>

  <footer class="footer-band">
    <div class="network-art" role="img" aria-label="Abstract network of connected nodes and lines"></div>

    <div class="contact contact--address">
      <span class="contact-icon">
        <svg viewBox="0 0 24 24"><path d="M12 2a7 7 0 0 0-7 7c0 4.5 7 13 7 13s7-8.5 7-13a7 7 0 0 0-7-7z" fill="var(--brand-blue)"/><circle cx="12" cy="9" r="3" fill="var(--white)"/></svg>
      </span>
      <div><p class="contact-label">Visit Us here</p><p class="contact-value">Your address here</p></div>
    </div>

    <div class="contact contact--website">
      <span class="contact-icon">
        <svg viewBox="0 0 24 24" fill="none" stroke="var(--brand-blue)" stroke-width="1.2"><circle cx="12" cy="12" r="9"/><ellipse cx="12" cy="12" rx="4" ry="9"/><path d="M3 12h18M12 3v18M5 7h14M5 17h14"/></svg>
      </span>
      <div><p class="contact-label">Visit Our Website</p><p class="contact-value">www.northgatecyber.com</p></div>
    </div>

    <div class="contact contact--phone">
      <span class="contact-icon">
        <svg viewBox="0 0 24 24"><path d="M6.6 10.8a15 15 0 0 0 6.6 6.6l2.2-2.2a1 1 0 0 1 1-.25 11.4 11.4 0 0 0 3.6.6 1 1 0 0 1 1 1V20a1 1 0 0 1-1 1A17 17 0 0 1 3 4a1 1 0 0 1 1-1h3.5a1 1 0 0 1 1 1c0 1.25.2 2.45.6 3.6a1 1 0 0 1-.25 1z" fill="var(--brand-blue)"/></svg>
      </span>
      <div><p class="contact-label">Office Number</p><p class="contact-value">+009XXXXXXXX</p></div>
    </div>

    <div class="contact contact--email">
      <span class="contact-icon">
        <svg viewBox="0 0 24 24" fill="none" stroke="var(--brand-blue)" stroke-width="1.4"><rect x="3" y="6" width="18" height="12" rx="2"/><path d="M3.5 7l8.5 6 8.5-6"/></svg>
      </span>
      <div><p class="contact-label">Email Address</p><p class="contact-value">mara@northgatecyber.com</p></div>
    </div>
  </footer>
</main>
</body>
</html>
```